Artwork for Space/Ambient/Drone synthesizer music

Art work is needed for a Collection of ambient type synthesizer soundtrack type of music. Title of album is Driftworks Vol. 1. This album's theme were to be kept as Movie music & Game music.

Looking for art reminiscent of Bram Toller retro futuristic look. Open to any ideas but I would like to see primarily sci-fi themes. I would like to have my logo either top center or bottom center and title of album top center or bottom center.

Online distributor requires art to be 2000 x 2000 at minimum but larger is preferable and no bigger than 10mb.

Track list with time is as follows:

1. Quiet Harbor 05:20
2. Tidewater 10:09
3. Lanterns 02:31
4. Ember 04:39
5. Copper Orchard 03:55
6. Velvet Engine 03:13
7. Marigolds 03:40
8. Overgrown 06:03
9. Woodcutters 02:06

I have uploaded 7 images by Bram Toller as reference for you (do not use those as I don't have rights to them). My logo is also uploaded for you to use in the art.

Target Market(s)

Synthwave. Retrowave. Ambient/Drone

Industry/Entity Type

Music Download

Font styles to use
Decorative

Colors

Designer to choose colors to be used in the design.

Requirements
Must have
• My logo (provided). Can change color of logo to fit art work.
Nice to have
• Abstract art is welcome.
Should not have
• No drug references. No death references. No references to countries. No graffiti style of art. No vector 80s graphics. No prominent faces. No religious references.

```html
<!DOCTYPE html>
<html lang="en">
<head>
<meta charset="utf-8">
<title>Driftworks Vol. 1 — Inlay and Disc</title>
<link rel="stylesheet" href="https://fonts.googleapis.com/css2?family=Bitter:wght@600&display=swap">
<style>
  :root {
    --backdrop: #cdc4a6;
    --ink-light: #f3f1ea;
    --bronze: #6e5a44;
    --umber: #3a3128;
    --night: #0e1119;
    --indigo: #1d2a4a;
    --steel: #5a6b85;
    --haze: #8d97a6;
    --glow: #e2defa;
    --logo-lilac: #9a96dc;
    --hub: #8a8c90;
  }
  html, body {
    margin: 0;
    padding: 0;
    width: 1200px;
    height: 900px;
    overflow: hidden;
    background: var(--backdrop);
  }
  .spread {
    position: relative;
    width: 1200px;
    height: 900px;
  }
  .inlay {
    position: absolute;
    left: 95px;
    top: 227px;
    width: 467px;
    height: 446px;
    overflow: hidden;
  }
  .inlay-art {
    position: absolute;
    inset: 0;
    display: block;
  }
  .tracklist {
    position: absolute;
    right: 130px;
    top: 70px;
    margin: 0;
    padding: 0;
    list-style: none;
    text-align: right;
    font-family: "Bitter", Georgia, serif;
    font-weight: 600;
    font-size: 16px;
    letter-spacing: 0.4px;
    line-height: 35px;
    color: var(--ink-light);
  }
  .disc {
    position: absolute;
    left: 638px;
    top: 217px;
    width: 466px;
    height: 466px;
  }
  .disc svg { display: block; }
  .label-name {
    font-family: "Bitter", Georgia, serif;
    font-weight: 600;
    font-size: 17px;
    letter-spacing: 0.4px;
    fill: var(--logo-lilac);
  }
  .album-title {
    font-family: "Bitter", Georgia, serif;
    font-weight: 600;
    font-size: 17px;
    letter-spacing: 0.4px;
    fill: var(--ink-light);
  }
</style>
</head>
<body>
<main class="spread">
  <section class="inlay" aria-label="Tracklist inlay">
    <svg class="inlay-art" width="467" height="446" viewBox="0 0 467 446" role="img" aria-label="Abstract weathered sci-fi horizon: bronze haze over a dark city band with a glowing scan line">
      <defs>
        <linearGradient id="inlaySky" x1="0" y1="0" x2="0" y2="1">
          <stop offset="0" stop-color="#6b5844"/>
          <stop offset="0.3" stop-color="#4a3d31"/>
          <stop offset="0.55" stop-color="#15171d"/>
          <stop offset="0.78" stop-color="#1f2d52"/>
          <stop offset="1" stop-color="#0c0e15"/>
        </linearGradient>
        <linearGradient id="inlayEdge" x1="0" y1="0" x2="1" y2="0">
          <stop offset="0" stop-color="#0c0e14" stop-opacity="0.9"/>
          <stop offset="1" stop-color="#0c0e14" stop-opacity="0"/>
        </linearGradient>
      </defs>
      <rect width="467" height="446" fill="url(#inlaySky)"/>
      <rect width="60" height="446" fill="url(#inlayEdge)"/>
      <rect x="0" y="300" width="467" height="14" fill="#0b0d13" opacity="0.55"/>
      <rect x="30" y="332" width="437" height="10" fill="#0b0d13" opacity="0.6"/>
      <rect x="140" y="360" width="327" height="8" fill="#0b0d13" opacity="0.7"/>
      <rect x="0" y="380" width="280" height="6" fill="#2c3d6b" opacity="0.7"/>
      <rect x="0" y="400" width="467" height="14" fill="#243457" opacity="0.8"/>
      <rect x="0" y="419" width="467" height="2" fill="var(--glow)"/>
      <rect x="0" y="417" width="467" height="6" fill="var(--glow)" opacity="0.25"/>
      <rect x="0" y="426" width="467" height="8" fill="var(--haze)" opacity="0.6"/>
      <rect x="0" y="434" width="467" height="12" fill="#0c0e15"/>
    </svg>
    <ol class="tracklist">
      <li>1. Quiet Harbor 05:20</li>
      <li>2. Tidewater 10:09</li>
      <li>3. Lanterns 02:31</li>
      <li>4. Ember 04:39</li>
      <li>5. Copper Orchard 03:55</li>
      <li>6. Velvet Engine 03:13</li>
      <li>7. Marigolds 03:40</li>
      <li>8. Overgrown 06:03</li>
      <li>9. Woodcutters 02:06</li>
    </ol>
  </section>

  <section class="disc" aria-label="Disc face">
    <svg width="466" height="466" viewBox="0 0 466 466">
      <defs>
        <linearGradient id="discArt" x1="0" y1="0" x2="0" y2="1">
          <stop offset="0" stop-color="#5d4f40"/>
          <stop offset="0.35" stop-color="#1a1d25"/>
          <stop offset="0.6" stop-color="#24304f"/>
          <stop offset="0.8" stop-color="#56616f"/>
          <stop offset="1" stop-color="#161920"/>
        </linearGradient>
        <clipPath id="discClip"><circle cx="233" cy="233" r="231"/></clipPath>
      </defs>
      <g clip-path="url(#discClip)" role="img" aria-label="Abstract weathered sci-fi horizon continuing the inlay artwork">
        <rect width="466" height="466" fill="url(#discArt)"/>
        <rect x="0" y="150" width="200" height="30" fill="#0b0d13" opacity="0.5"/>
        <rect x="260" y="240" width="206" height="6" fill="#0b0d13" opacity="0.6"/>
        <rect x="0" y="285" width="466" height="14" fill="#2c3d6b" opacity="0.8"/>
        <rect x="0" y="303" width="466" height="6" fill="var(--glow)" opacity="0.25"/>
        <rect x="0" y="305" width="466" height="2" fill="var(--glow)"/>
        <rect x="0" y="316" width="466" height="10" fill="var(--haze)" opacity="0.55"/>
        <rect x="0" y="340" width="466" height="6" fill="#0b0d13" opacity="0.5"/>
        <rect x="0" y="430" width="466" height="36" fill="#0b0d13" opacity="0.5"/>
      </g>
      <circle cx="233" cy="233" r="231" fill="none" stroke="#0b0c10" stroke-width="3"/>
      <circle cx="233" cy="233" r="73" fill="#d8d9dc"/>
      <circle cx="233" cy="233" r="67" fill="var(--hub)"/>
      <circle cx="233" cy="233" r="22" fill="#eeeeee"/>
      <circle cx="233" cy="233" r="14" fill="#cfcfcf"/>
      <text class="label-name" x="233" y="72" text-anchor="middle">Kestrel Tone</text>
      <text class="album-title" x="233" y="400" text-anchor="middle">Driftworks Vol. 1</text>
    </svg>
  </section>
</main>
</body>
</html>
```